Harvest Fresh Wonders (Postcard)

Looking for a professional post card (5x7) - front and back, graphic design to promote a campaign called Harvest Fresh Wonders. The goal is to promote Orthodontics in our dental practice for our existing and new patients.

```html
<!DOCTYPE html>
<html lang="en">
<head>
<meta charset="utf-8">
<title>Harvest Fresh Wonders – Postcard</title>
<link rel="stylesheet" href="https://fonts.googleapis.com/css2?family=Poppins:wght@400;500;600;700;800&family=Oswald:wght@700&family=Yellowtail&display=swap">
<style>
  :root {
    --navy: #243a8a;
    --orange: #f0914a;
    --white: #ffffff;
    --backdrop: #2b2b2b;
    --photo-light: #dfe5ee;
    --photo-mid: #c9d2df;
    --rule: #4a4f63;
  }
  * { box-sizing: border-box; margin: 0; padding: 0; }
  html, body {
    width: 1200px; height: 587px; overflow: hidden;
    background: var(--backdrop);
    font-family: "Poppins", sans-serif;
  }
  .card {
    position: absolute; top: 116px;
    width: 499px; height: 356px;
    background: var(--white); overflow: hidden;
  }
  .card--front { left: 80px; }
  .card--back { left: 622px; }
  .card-shapes { position: absolute; inset: 0; }
  .abs { position: absolute; white-space: nowrap; }

  .brand { display: flex; align-items: center; gap: 7px; color: var(--navy); font-weight: 500; font-size: 19px; letter-spacing: 0.5px; line-height: 1; }
  .brand-dot { width: 14px; height: 14px; border-radius: 50%; background: var(--orange); }

  .headline-script { font-family: "Yellowtail", cursive; color: var(--orange); font-size: 44px; line-height: 1; }
  .headline-bold { font-family: "Oswald", sans-serif; font-weight: 700; color: var(--navy); font-size: 28px; line-height: 1; letter-spacing: 0.2px; transform: skewX(-8deg) scaleY(1.2); transform-origin: left top; }
  .headline-with { display: flex; align-items: baseline; gap: 8px; line-height: 1; }
  .headline-with .script { font-family: "Yellowtail", cursive; color: var(--orange); font-size: 28px; }
  .headline-with .name { color: var(--navy); font-weight: 700; font-size: 14px; }

  .offer-front { color: var(--white); line-height: 1; }
  .offer-front .enjoy { font-size: 21px; font-weight: 500; }
  .offer-front .amount { font-size: 31px; font-weight: 700; margin-left: 8px; }
  .offer-front .treatment { font-size: 15px; font-weight: 600; letter-spacing: 0.2px; }

  .tagline { color: var(--white); font-weight: 700; font-size: 20.5px; letter-spacing: 0.2px; line-height: 31px; }

  .contact-call { display: flex; align-items: center; gap: 5px; color: var(--navy); }
  .icon-box { background: var(--orange); border-radius: 4px; display: flex; align-items: center; justify-content: center; }
  .call-label { font-size: 10.5px; font-weight: 500; line-height: 1.1; }
  .call-number { font-size: 14px; font-weight: 700; line-height: 1.1; }
  .schedule-small { color: var(--navy); font-size: 9.5px; font-weight: 500; line-height: 1.2; }
  .schedule-big { color: var(--navy); font-size: 13.5px; font-weight: 600; line-height: 1.1; }
  .accent { color: var(--orange); }
  .web { color: var(--navy); font-weight: 700; font-size: 11px; line-height: 1; }

  .offer-back { line-height: 1; }
  .offer-back .enjoy { color: var(--white); font-size: 23px; font-weight: 500; }
  .offer-back .amount { color: var(--navy); font-size: 35px; font-weight: 800; margin-left: 6px; }
  .offer-back .ortho { color: var(--navy); font-size: 21.5px; font-weight: 800; }
  .offer-back .treat { color: var(--white); font-size: 28px; font-weight: 700; }

  .back-schedule-small { color: var(--navy); font-size: 11px; font-weight: 600; line-height: 1.05; }
  .back-schedule-big { color: var(--navy); font-size: 14px; font-weight: 600; line-height: 1; }
  .back-call-label { color: var(--navy); font-size: 14px; font-weight: 500; line-height: 1; }
  .back-call-number { color: var(--navy); font-size: 20px; font-weight: 700; line-height: 1.1; }
  .back-web { color: var(--navy); font-size: 14px; font-weight: 600; letter-spacing: 3px; line-height: 1; }
</style>
</head>
<body>

<section class="card card--front" aria-label="Postcard front">
  <svg class="card-shapes" width="499" height="356" viewBox="0 0 499 356">
    <defs>
      <linearGradient id="photoTone" x1="0" y1="0" x2="1" y2="1">
        <stop offset="0" stop-color="#dfe5ee"/>
        <stop offset="1" stop-color="#c9d2df"/>
      </linearGradient>
    </defs>
    <polygon role="img" aria-label="Photo of a smiling patient touching her cheeks" points="286,0 499,0 499,256 296,256 221,66" fill="url(#photoTone)"/>
    <polyline points="270,0 201,66 282,262" fill="none" stroke="var(--navy)" stroke-width="9"/>
    <polygon points="0,196 238,196 260,256 0,256" fill="var(--orange)"/>
    <rect x="0" y="261" width="499" height="31" fill="var(--navy)"/>
    <rect x="158" y="307" width="2" height="36" fill="var(--orange)"/>
    <rect x="349" y="307" width="2" height="36" fill="var(--orange)"/>
  </svg>

  <div class="abs brand" style="left:27px; top:34px;"><span class="brand-dot"></span>Brightway Dental</div>

  <div class="abs headline-script" style="left:42px; top:80px;">Harvest</div>
  <div class="abs headline-bold" style="left:22px; top:122px;">FRESH WONDERS</div>
  <div class="abs headline-with" style="left:18px; top:158px;"><span class="script">With</span><span class="name">Brightway Dental</span></div>

  <div class="abs offer-front" style="left:22px; top:202px;"><span class="enjoy">Enjoy</span><span class="amount">$500</span></div>
  <div class="abs offer-front" style="left:22px; top:237px;"><span class="treatment">ORTHODONTIC TREATMENT</span></div>

  <div class="abs tagline" style="left:22px; top:261px;">OFFERING BRACES FOR YOUR BEST SMILE!</div>

  <div class="abs contact-call" style="left:22px; top:310px;">
    <div class="icon-box" style="width:23px; height:23px;">
      <svg width="14" height="14" viewBox="0 0 24 24"><path d="M6.6 10.8a15 15 0 0 0 6.6 6.6l2.2-2.2a1 1 0 0 1 1-.25 11.4 11.4 0 0 0 3.6.57 1 1 0 0 1 1 1V20a1 1 0 0 1-1 1A17 17 0 0 1 3 4a1 1 0 0 1 1-1h3.5a1 1 0 0 1 1 1c0 1.25.2 2.45.57 3.57a1 1 0 0 1-.25 1z" fill="var(--white)"/></svg>
    </div>
    <div><div class="call-label">Call Today</div><div class="call-number">014 555 0192</div></div>
  </div>
  <div class="abs" style="left:171px; top:311px;">
    <div class="schedule-small">TO SCHEDULE YOUR APPOINTMENT</div>
    <div class="schedule-big">OR <span class="accent">FREE CONSULTATION</span></div>
  </div>
  <div class="abs web" style="left:360px; top:320px;">BrightwayDental.com</div>
</section>

<section class="card card--back" aria-label="Postcard back">
  <svg class="card-shapes" width="499" height="356" viewBox="0 0 499 356">
    <polygon points="0,75 190,75 211,148 190,174 0,174" fill="var(--orange)"/>
    <polyline points="198,75 225,148 199,174" fill="none" stroke="var(--navy)" stroke-width="6"/>
    <rect x="370" y="38" width="93" height="101" fill="none" stroke="var(--rule)" stroke-width="1" stroke-dasharray="8 6"/>
    <g stroke="var(--rule)" stroke-width="1">
      <line x1="249" y1="192" x2="462" y2="192"/>
      <line x1="249" y1="232" x2="462" y2="232"/>
      <line x1="249" y1="271" x2="462" y2="271"/>
      <line x1="249" y1="311" x2="462" y2="311"/>
    </g>
    <g fill="none" stroke="var(--navy)" stroke-width="2">
      <rect x="30" y="189" width="33" height="28" rx="4"/>
      <line x1="37" y1="186" x2="37" y2="192"/>
      <line x1="56" y1="186" x2="56" y2="192"/>
    </g>
    <g fill="none" stroke="var(--orange)" stroke-width="1.6">
      <rect x="35" y="197" width="6" height="5"/>
      <rect x="44" y="197" width="6" height="5"/>
      <rect x="53" y="197" width="6" height="5"/>
      <rect x="35" y="206" width="6" height="5"/>
      <rect x="44" y="206" width="6" height="5"/>
    </g>
  </svg>

  <div class="abs brand" style="left:30px; top:34px;"><span class="brand-dot"></span>Brightway Dental</div>

  <div class="abs offer-back" style="left:24px; top:82px;"><span class="enjoy">Enjoy</span><span class="amount">$500</span></div>
  <div class="abs offer-back" style="left:23px; top:118px;"><span class="ortho">ORTHODONTIC</span></div>
  <div class="abs offer-back" style="left:23px; top:141px;"><span class="treat">TREATMENT</span></div>

  <div class="abs" style="left:69px; top:192px;">
    <div class="back-schedule-small">TO SCHEDULE</div>
    <div class="back-schedule-small">YOUR APPOINTMENT</div>
  </div>
  <div class="abs back-schedule-big" style="left:30px; top:222px;">OR <span class="accent">FREE CONSULTATION</span></div>

  <div class="abs icon-box" style="left:30px; top:248px; width:37px; height:37px; border-radius:6px;">
    <svg width="22" height="22" viewBox="0 0 24 24"><path d="M6.6 10.8a15 15 0 0 0 6.6 6.6l2.2-2.2a1 1 0 0 1 1-.25 11.4 11.4 0 0 0 3.6.57 1 1 0 0 1 1 1V20a1 1 0 0 1-1 1A17 17 0 0 1 3 4a1 1 0 0 1 1-1h3.5a1 1 0 0 1 1 1c0 1.25.2 2.45.57 3.57a1 1 0 0 1-.25 1z" fill="var(--white)"/></svg>
  </div>
  <div class="abs" style="left:70px; top:252px;">
    <div class="back-call-label">Call Today</div>
    <div class="back-call-number">014 555 0192</div>
  </div>

  <div class="abs back-web" style="left:30px; top:307px;">BrightwayDental.com</div>
</section>

</body>
</html>
```